Business Card Design

We are a contracting firm, 95% of my work is interior renovations.... but also don't want to preclude the idea of doing exterior work if it arises. I Need a business card that says I am the ultimate professional. There is a per-determined notion that all contractors are shady, unreliable, etc. Being that most of my work is in Manhattan, I would like to give the impression of fresh, modern, sleek, design/build firm.

Target Market(s)

young couples 25-40

Industry/Entity Type

Business

Contact Information for Business Card

PeterHollowayInteriors LLC
27 North Brandel Street
Marsh Hollow NY 11492
718-555-0142
646-555-0187- cell
www.phbwx.com
ph@phbwx.com
Peter Holloway

Requirements
Should not have
• do not want to give the impression of a "bargain basement store"

```html
<!DOCTYPE html>
<html lang="en">
<head>
<meta charset="utf-8">
<title>PeterHollowayInteriors LLC – Business Card</title>
<link rel="stylesheet" href="https://fonts.googleapis.com/css2?family=Cutive+Mono&display=swap">
<style>
  :root {
    --page: #ffffff;
    --card: #0b0b0b;
    --ink: #f2f2f2;
    --accent: #c9968a;
  }
  html, body {
    margin: 0;
    padding: 0;
    width: 1200px;
    height: 702px;
    overflow: hidden;
    background: var(--page);
  }
  .canvas {
    position: relative;
    width: 1200px;
    height: 702px;
    background: var(--page);
  }
  .card {
    position: absolute;
    left: 31px;
    top: 24px;
    width: 1143px;
    height: 653px;
    background: var(--card);
    font-family: "Cutive Mono", "Courier New", monospace;
    color: var(--ink);
  }
  .card p {
    position: absolute;
    margin: 0;
    white-space: nowrap;
    line-height: 1;
  }
  .company-name {
    left: 150px;
    top: 83px;
    font-size: 30px;
    letter-spacing: 6.5px;
  }
  .details {
    left: 150px;
    font-size: 24px;
    letter-spacing: 4.8px;
  }
  .address-line-1 { top: 250px; }
  .address-line-2 { top: 289px; }
  .address-line-3 { top: 327px; }
  .phones        { top: 410px; }
  .web-contact   { top: 488px; }
  .brand-name {
    right: 44px;
    top: 34px;
    font-size: 40px;
    letter-spacing: 2px;
    color: var(--accent);
  }
</style>
</head>
<body>
  <div class="canvas">
    <section class="card" aria-label="PeterHollowayInteriors LLC business card">
      <p class="company-name">PeterHollowayInteriors</p>
      <p class="details address-line-1">LLC 27 North Brandel Street,</p>
      <p class="details address-line-2">Marsh Hollow,</p>
      <p class="details address-line-3">NY 11492</p>
      <p class="details phones">Tel- 718-555-0142 \ 646-555-0187</p>
      <p class="details web-contact">www.phbwx.com ph@phbwx.com Peter Holloway</p>
      <p class="brand-name">PH</p>
    </section>
  </div>
</body>
</html>
```